Business Card Design Project : Ferncliff Media

In preparation for market launch, Whistler's Ferncliff Media require the development of a business card. Ferncliff Media is a Community online publishing web portal. We provide the the city of Whistler located in B.C. (Canada) business directories, News, Classified ads, News, Events and blogs etc.

The main focus of the brand is to help local businesses to corporate with their online advertisement and marketing. Meeting our clients face to face is a must (B2B).

Target Market(s)

The target market is B2B customers. Business Owners to Marketing, advertising Managers

Industry/Entity Type

Business

Requirements
Must have
• - The business card will be two sided.
the BACK side will have our logo which consist of (icon, url,slogan) submited. The logo will be middle and centred.

The FRONT side should have company details:

Company Legal Name: TALLPINE FERNCLIFF MEDIA

Dale Morrow
Director of Sales & Marketing

www.tallpineferncliff.biz
dale@tallpineferncliff.biz

Phone: 604 555 0138
#2217 - 581 E. Harlow Ave.
Vancouver, B.C. V6N2K4 Canada
Nice to have
• - For the "FRONT" side of our business card. You can separate or re-arrange with our logo components (icon, logo,slogan). It does not have to be together.

Also our company legal name is rather long so arrange or organize the name in a way to make it shorter. Your experience and creativity will have to come in play.
Should not have
• should not have other colors beside logo color and black text (2 colors). Also nothing Three dimensional

```html
<!DOCTYPE html>
<html lang="en">
<head>
<meta charset="utf-8">
<title>Tallpine Ferncliff Media – Business Card</title>
<link href="https://fonts.googleapis.com/css2?family=Arimo:wght@400;700&family=Open+Sans:wght@400;700&display=swap" rel="stylesheet">
<style>
  :root {
    --brand-blue: #2a7cc7;
    --ink: #111111;
    --paper: #ffffff;
    --pattern-tint: #eef2f8;
    --stage: #e4e5e7;
  }
  * { box-sizing: border-box; margin: 0; padding: 0; }
  html, body { width: 1200px; height: 871px; overflow: hidden; }
  body {
    background: var(--stage);
    font-family: "Arimo", Arial, sans-serif;
    position: relative;
  }
  .card {
    position: absolute;
    top: 287px;
    width: 520px;
    height: 297px;
    background: var(--paper);
    overflow: hidden;
    box-shadow: 0 2px 8px rgba(0,0,0,0.12);
  }
  .card--back { left: 50px; }
  .card--front { left: 630px; }
  .pattern-fill {
    position: absolute; inset: 0;
    background: linear-gradient(160deg, var(--paper) 0%, var(--pattern-tint) 55%, var(--paper) 100%);
  }

  /* Back side */
  .back-mark {
    position: absolute; left: 0; right: 0; top: 62px;
    display: flex; align-items: center; justify-content: center; gap: 12px;
  }
  .mark-dot { width: 34px; height: 34px; border-radius: 50%; background: var(--brand-blue); }
  .mark-name {
    font-family: "Arimo", Arial, sans-serif; font-weight: 700;
    color: var(--brand-blue); font-size: 30px; letter-spacing: 0.5px;
  }
  .back-url {
    position: absolute; left: 0; right: 0; top: 116px; text-align: center;
    font-family: "Open Sans", Arial, sans-serif; font-weight: 700;
    font-size: 26px; color: var(--ink);
  }
  .back-slogan {
    position: absolute; left: 0; right: 0; top: 152px; text-align: center;
    font-family: "Open Sans", Arial, sans-serif; font-size: 17px; color: var(--brand-blue);
  }
  .back-services {
    position: absolute; left: 0; right: 0; top: 222px; text-align: center;
    font-size: 9.5px; font-weight: 700; letter-spacing: 0.6px; color: var(--ink);
  }
  .stripe { position: absolute; left: 0; right: 0; }
  .back-stripe-black { top: 240px; height: 12px; background: var(--ink); }
  .back-stripe-blue { top: 258px; height: 7px; background: var(--brand-blue); }

  /* Front side */
  .company-name {
    position: absolute; left: 22px; top: 62px;
    font-weight: 700; font-size: 19px; color: var(--ink);
  }
  .info-band {
    position: absolute; left: 0; top: 92px; width: 330px; height: 122px;
    background: var(--brand-blue); color: var(--paper);
    padding: 8px 22px;
  }
  .person-name { font-weight: 700; font-size: 12.5px; letter-spacing: 0.4px; }
  .person-title { font-size: 9.5px; margin-top: 2px; }
  .contact-line { display: flex; align-items: center; gap: 7px; font-size: 10.5px; margin-top: 6px; }
  .contact-line + .contact-line { margin-top: 3px; }
  .contact-icon { width: 10px; height: 10px; flex: none; }
  .address { font-size: 9.5px; line-height: 1.3; margin-top: 6px; }
  .front-mark {
    position: absolute; left: 330px; top: 92px; width: 190px; height: 122px;
    background: var(--brand-blue);
    border-radius: 0 0 0 60px;
    display: flex; align-items: center; justify-content: center; gap: 8px;
  }
  .front-mark .mark-dot { width: 20px; height: 20px; background: var(--paper); }
  .front-mark .mark-name { color: var(--paper); font-size: 17px; }
  .front-stripe-black { right: auto; top: 226px; height: 10px; width: 250px; background: var(--ink); }
  .front-stripe-blue { right: auto; top: 240px; height: 5px; width: 250px; background: var(--brand-blue); }
  .front-url {
    position: absolute; right: 20px; top: 224px;
    font-family: "Open Sans", Arial, sans-serif; font-weight: 700;
    font-size: 17px; color: var(--ink); white-space: nowrap;
  }
  .front-slogan {
    position: absolute; right: 20px; top: 248px;
    font-family: "Open Sans", Arial, sans-serif; font-size: 13px; color: var(--brand-blue);
  }
</style>
</head>
<body>

<section class="card card--back" aria-label="Card back">
  <div class="pattern-fill" role="img" aria-label="Faint repeating brand pattern in pale blue"></div>
  <div class="back-mark">
    <span class="mark-dot"></span>
    <span class="mark-name">Ferncliff Media</span>
  </div>
  <p class="back-url">www.tallpineferncliff.biz</p>
  <p class="back-slogan">Your information gateway</p>
  <p class="back-services">COMMUNITY NEWS &amp; EVENTS · CLASSIFIEDS · BLOGS</p>
  <div class="stripe back-stripe-black"></div>
  <div class="stripe back-stripe-blue"></div>
</section>

<section class="card card--front" aria-label="Card front">
  <div class="pattern-fill" role="img" aria-label="Faint repeating brand pattern in pale blue"></div>
  <h1 class="company-name">Tallpine Ferncliff Media</h1>
  <div class="info-band">
    <p class="person-name">DALE MORROW</p>
    <p class="person-title">Director of Sales &amp; Marketing</p>
    <p class="contact-line">
      <svg class="contact-icon" viewBox="0 0 10 10" aria-hidden="true">
        <rect x="2.5" y="0.5" width="5" height="9" rx="1" fill="none" stroke="#fff" stroke-width="1"/>
        <circle cx="5" cy="8" r="0.6" fill="#fff"/>
      </svg>
      604 555 0138
    </p>
    <p class="contact-line">
      <svg class="contact-icon" viewBox="0 0 10 10" aria-hidden="true">
        <rect x="0.5" y="2" width="9" height="6.5" fill="#fff"/>
        <path d="M0.5 2 L5 5.8 L9.5 2" fill="none" stroke="#2a7cc7" stroke-width="0.9"/>
      </svg>
      dale@tallpineferncliff.biz
    </p>
    <p class="address">#2217 - 581 E. Harlow Ave.<br>Vancouver, B.C. V6N2K4 Canada</p>
  </div>
  <div class="front-mark">
    <span class="mark-dot"></span>
    <span class="mark-name">Ferncliff Media</span>
  </div>
  <div class="stripe front-stripe-black"></div>
  <div class="stripe front-stripe-blue"></div>
  <p class="front-url">www.tallpineferncliff.biz</p>
  <p class="front-slogan">Your information gateway</p>
</section>

</body>
</html>
```